Insurance company needs a business card design

We need a business card design for a Massachusetts-based insurance company Veloria Insurance, LLC. We provide auto insurance to Hispanic (Spanish- or Portuguese-speaking) immigrants in the United States. We will give these business cards to auto dealers where such customers typically go to purchase vehicles. We will provide a solution to the dealers to provide easy insurance to the customers buying cars at their dealerships. Veloria is the Spanish word for protection.
Contact Information for Business Card
Name, Designation, Company Name, Address, Phone Number, Email, Website
Look and feel
Each slider illustrates characteristics of the customer's brand and the style your logo design should communicate.

```html
<!DOCTYPE html>
<html lang="en">
<head>
<meta charset="utf-8">
<title>Veloria Insurance – Business Card</title>
<link rel="stylesheet" href="https://fonts.googleapis.com/css2?family=Montserrat:wght@600;700&family=Figtree:wght@400;500&display=swap">
<style>
  :root {
    --navy: #0b4a7e;
    --navy-deep: #063a66;
    --orange: #e08a17;
    --ink: #1c1c1c;
    --card: #fbfaf8;
    --backdrop: #e9e5df;
    --band-text: #e6dccb;
  }
  html, body {
    margin: 0;
    width: 1200px;
    height: 969px;
    overflow: hidden;
    background: var(--backdrop);
  }
  .card {
    position: absolute;
    left: 60px;
    top: 177px;
    width: 1080px;
    height: 615px;
    background: var(--card);
    border: 1px solid #d8d3cb;
    border-radius: 34px;
    overflow: hidden;
    box-shadow: 0 10px 30px rgba(0,0,0,0.08);
  }
  .brand {
    position: absolute;
    left: 0;
    right: 0;
    top: 140px;
    display: flex;
    justify-content: center;
    align-items: center;
    gap: 26px;
  }
  .brand-mark {
    width: 92px;
    height: 92px;
    background: var(--orange);
  }
  .brand-name {
    font-family: "Montserrat", sans-serif;
    font-weight: 700;
    font-size: 54px;
    letter-spacing: 2px;
    color: var(--navy);
    line-height: 1;
  }
  .person {
    position: absolute;
    right: calc(1080px - 462px);
    top: 352px;
    text-align: right;
  }
  .person-name {
    font-family: "Montserrat", sans-serif;
    font-weight: 700;
    font-size: 32px;
    color: var(--orange);
    margin: 0 0 12px;
    line-height: 1.1;
  }
  .person-role, .person-company {
    font-family: "Figtree", sans-serif;
    font-size: 26px;
    color: var(--ink);
    margin: 0;
    line-height: 1.35;
  }
  .divider {
    position: absolute;
    left: 485px;
    top: 343px;
    width: 2px;
    height: 108px;
    background: var(--orange);
  }
  .contacts {
    position: absolute;
    left: 520px;
    top: 345px;
    margin: 0;
    padding: 0;
    list-style: none;
  }
  .contact {
    display: flex;
    align-items: center;
    gap: 14px;
    height: 39px;
    font-family: "Figtree", sans-serif;
    font-size: 26px;
    color: var(--ink);
  }
  .contact svg {
    width: 22px;
    height: 22px;
    flex: none;
  }
  .address-band {
    position: absolute;
    left: 0;
    right: 0;
    top: 516px;
    height: 62px;
    background: linear-gradient(90deg, var(--navy-deep), var(--navy) 50%, var(--navy-deep));
    display: flex;
    justify-content: center;
    align-items: center;
    font-family: "Figtree", sans-serif;
    font-weight: 500;
    font-size: 22px;
    color: var(--band-text);
  }
</style>
</head>
<body>
  <main class="card">
    <div class="brand">
      <div class="brand-mark"></div>
      <div class="brand-name">VELORIA INSURANCE</div>
    </div>

    <div class="person">
      <p class="person-name">DALEN WHITCOMBE</p>
      <p class="person-role">Co-Founder</p>
      <p class="person-company">Veloria Insurance, LLC</p>
    </div>

    <div class="divider"></div>

    <ul class="contacts">
      <li class="contact">
        <svg viewBox="0 0 24 24" aria-hidden="true"><path fill="var(--orange)" d="M6.6 10.8a15.1 15.1 0 0 0 6.6 6.6l2.2-2.2c.3-.3.7-.4 1-.2 1.1.4 2.3.6 3.6.6.6 0 1 .4 1 1V20c0 .6-.4 1-1 1A17 17 0 0 1 3 4c0-.6.4-1 1-1h3.5c.6 0 1 .4 1 1 0 1.3.2 2.5.6 3.6.1.3 0 .7-.2 1z"/></svg>
        <span>9896-555-0148</span>
      </li>
      <li class="contact">
        <svg viewBox="0 0 24 24" aria-hidden="true"><path fill="var(--orange)" d="M2 5h20v14H2z"/><path fill="none" stroke="#fff" stroke-width="1.6" d="M2.5 5.5 12 13l9.5-7.5"/></svg>
        <span>info@veloriainsurance.com</span>
      </li>
      <li class="contact">
        <svg viewBox="0 0 24 24" aria-hidden="true"><circle cx="12" cy="12" r="10" fill="var(--orange)"/><path fill="none" stroke="#fff" stroke-width="1.3" d="M2 12h20M12 2c3 3 3 17 0 20M12 2c-3 3-3 17 0 20"/></svg>
        <span>www.veloriainsurance.com</span>
      </li>
    </ul>

    <div class="address-band">Brightway Plaza 2100 Harbor Lane Suite 310</div>
  </main>
</body>
</html>
```